Web Page Design for a Website that Provides Tutoring

I am looking to create an online tutoring website. The website will allow parents or students to contact tutors with a view to instructing them to tutor themselves or their children.

The name of the website is LendYourLessons.

This brief is to create the design for one of the web pages for this web site. I am hoping the same designer will be available to design other pages.

The page I want designed is one of the more complex and I have attached the design as an excel spreadsheet. The web page needs to include all the items on this page but if you want to change the positioning of the items then Im fine with that.

I recently had two logos created for this website. My favourite is the one with a mortar board but im not sure I like the colours. I have attached both of these logos and you can use either of them, change the colours or create something different. I just want a design pleasing to the eye. If the logo is changed I would like that in a seperate file.

So can you please submit designs for this page. I have attached the two logos which you can use, change or if you feel you have a better idea then you can use that.

On the spreadsheet the Send Message, Favourite etc are buttons.

Target Market(s)

People who want to better themselves.
Possible middle class to upper class.

Industry/Entity Type

Tutoring

Number of Pages Required

1 page

Requirements
Must have
• The designs must have alot of the information attached in the spreadsheet.

```html
<!DOCTYPE html>
<html lang="en">
<head>
<meta charset="utf-8">
<title>LendYourLessons – Tutor Profile</title>
<link rel="stylesheet" href="https://fonts.googleapis.com/css2?family=Comfortaa:wght@400;700&family=Open+Sans:wght@400;600&display=swap">
<style>
:root{
  --orange:#f7941d;
  --orange-light:#fbb316;
  --text:#555555;
  --text-dark:#333333;
  --muted:#777777;
  --line:#e6e6e6;
  --dark:#4a4a4a;
  --green:#8dc63f;
  --red:#d0312d;
  --purple:#a334c7;
  --blue:#2e8fcf;
  --star:#f9a21b;
  --panel:#ededed;
}
*{box-sizing:border-box;margin:0;padding:0}
html,body{width:1200px;height:1174px;overflow:hidden;background:#fff}
body{position:relative;font-family:"Comfortaa",sans-serif;color:var(--text)}
.abs{position:absolute}

/* header */
.site-header{left:0;top:0;width:1200px;height:72px;border-bottom:1px solid #d5d5d5}
.brand{left:139px;top:16px;display:flex;align-items:center;gap:8px;font:700 31px "Comfortaa",sans-serif;color:var(--orange)}
.brand-dot{width:14px;height:14px;border-radius:50%;background:var(--orange)}
.social{right:106px;top:30px;display:flex;gap:10px}
.social span{width:13px;height:13px;border-radius:50%;background:#666}
.main-nav{left:139px;top:92px;display:flex;gap:22px;font:600 15px "Open Sans",sans-serif;letter-spacing:.5px;color:#666}
.main-nav .active{color:var(--orange)}
.login{right:106px;top:92px;font:600 15px "Open Sans",sans-serif;letter-spacing:.5px;color:#666;display:flex;align-items:center;gap:6px}

/* hero */
.hero-band{left:0;top:126px;width:1200px;height:116px;background:linear-gradient(90deg,var(--orange-light),var(--orange) 50%,var(--orange-light))}
.avatar{border-radius:50%;background:radial-gradient(circle at 50% 40%,#b08a72,#5b4336 60%,#2f2520)}
.avatar-main{left:138px;top:149px;width:148px;height:148px;border:3px solid #fff}
.tutor-name{left:310px;top:158px;font:700 38px "Comfortaa",sans-serif;color:#fff}
.tutor-role{left:310px;top:200px;font:400 17px "Comfortaa",sans-serif;color:#fff}
.tutor-role b{font-weight:700}

/* meta */
.meta{left:162px;display:flex;gap:8px;font-size:10px;line-height:12px;color:var(--text-dark)}
.btn{display:flex;align-items:center;justify-content:center;border-radius:4px;color:#fff;font:700 14px "Comfortaa",sans-serif}
.btn-feedback{left:163px;top:391px;width:128px;height:40px;background:var(--red);box-shadow:inset 0 -3px 0 #a82320}

.bio{left:312px;top:266px;width:480px;font-size:9.6px;line-height:12px;text-align:justify;color:var(--muted)}
.bio p+p{margin-top:12px}

/* booking */
.booking{left:828px;top:186px;width:238px;height:360px;border-radius:6px;background:#fff;box-shadow:0 0 0 1px #e4e4e4;overflow:hidden}
.price{height:48px;background:var(--dark);color:#fff;display:flex;align-items:center;justify-content:center;gap:8px}
.price strong{font:700 20px "Comfortaa",sans-serif}
.price small{font-size:9.5px}
.booking-label{text-align:center;font:700 10px "Comfortaa",sans-serif;color:var(--text-dark);margin-top:31px}
.field{position:absolute;left:18px;width:199px;height:42px;border:1px solid #e3e3e3;border-radius:4px;display:flex;align-items:center;justify-content:space-between;padding:0 15px;font-size:14px;color:#666}
.caret{font-size:11px;color:#555}
.btn-book{position:absolute;left:18px;top:263px;width:199px;height:45px;background:var(--green);box-shadow:inset 0 -3px 0 #6fa52a;font-size:13px}
.like{position:absolute;left:0;top:318px;width:238px;height:42px;background:var(--panel);border-top:1px solid #ddd;display:flex;align-items:center;justify-content:center;gap:8px;font-size:9.5px;color:#888}

/* cards */
.card{border:1px solid #e8e8e8;border-radius:6px;background:#fff}
.score-card{left:154px;top:477px;width:632px;height:135px}
.score{left:0;top:22px;width:200px;text-align:center;font:700 56px "Open Sans",sans-serif;color:var(--text-dark);line-height:1}
.score-label{left:0;top:80px;width:200px;text-align:center;font:600 13px "Open Sans",sans-serif;color:var(--text-dark)}
.stars{display:flex;gap:3px}
.rating-list{list-style:none;font:400 11.5px "Open Sans",sans-serif;color:var(--text-dark)}
.rating-list li{display:flex;align-items:center;gap:9px;height:26px}

.section-title{font:700 18px "Comfortaa",sans-serif;color:var(--text-dark)}
.section-title span{font-weight:400}
.title-rule{width:42px;height:4px;background:var(--orange)}

.calendar-card{left:154px;top:638px;width:632px;height:296px}
.schedule{position:absolute;left:0;top:73px;width:630px;border-collapse:collapse;table-layout:fixed;font:400 11px "Open Sans",sans-serif;color:var(--muted)}
.schedule th{height:33px;font-weight:400;font-size:11.5px;border-left:1px solid var(--line);border-top:1px solid var(--line)}
.schedule th:first-child{border-left:0}
.schedule td{height:26.6px;border-left:1px solid var(--line);border-top:1px solid var(--line);padding:3px;text-align:center}
.schedule td:first-child{border-left:0;font-size:11.5px}
.slot{display:block;height:19px;line-height:19px;color:#fff;font-size:9.5px}
.open{background:var(--green)}
.taken{background:var(--red)}
.reserved{background:var(--blue)}
.closed{background:var(--purple)}

.review-name{left:284px;top:1060px;font:400 17px "Comfortaa",sans-serif;color:#555}
.review-date{left:637px;top:1086px;font-size:9.5px;color:#bbb}
.review-box{left:163px;top:1146px;width:623px;height:60px;border:1px solid #eee;border-radius:6px}
</style>
</head>
<body>

<header class="site-header abs">
  <div class="brand abs"><span class="brand-dot"></span>LendYourLessons</div>
  <div class="social abs" aria-label="Social links"><span></span><span></span><span></span></div>
</header>

<nav class="main-nav abs">
  <span>HOME</span><span class="active">SEARCH</span><span>STUDENT</span><span>TUTOR</span><span>ABOUT</span><span>CONTACT</span>
</nav>
<div class="login abs">
  <svg width="10" height="11" viewBox="0 0 10 11"><circle cx="5" cy="3" r="2.6" fill="#777"/><path d="M0 11c0-3.5 2-5 5-5s5 1.5 5 5z" fill="#777"/></svg>
  LOGIN / REGISTER
</div>

<div class="hero-band abs"></div>
<div class="avatar avatar-main abs" role="img" aria-label="Portrait photo of the tutor"></div>
<h1 class="tutor-name abs">Daniel Moreau</h1>
<p class="tutor-role abs"><b>Teacher</b> / Chemistry / Biology</p>

<div class="meta abs" style="top:318px">
  <svg width="20" height="22" viewBox="0 0 20 22"><rect x="1" y="1" width="15" height="20" rx="1" fill="none" stroke="#444" stroke-width="1.3"/><path d="M4 7h6M4 11h8M4 15h8" stroke="#444" stroke-width="1.2"/><path d="M10 7l2 2 5-5" fill="none" stroke="#444" stroke-width="1.3"/></svg>
  <div>Member Since<br>2009</div>
</div>
<div class="meta abs" style="top:352px">
  <svg width="20" height="20" viewBox="0 0 20 20" style="margin-top:4px"><circle cx="9" cy="9" r="7.5" fill="none" stroke="#8dc63f" stroke-width="1.5"/><circle cx="9" cy="9" r="5" fill="#8dc63f"/></svg>
  <div>Last Logged In<br>05/10/2016 - 10 am</div>
</div>
<div class="btn btn-feedback abs">Add feedback</div>

<div class="bio abs">
  <p>Lorem ipsum dolor sit amet enim. Etiam ullamcorper. Suspendisse a pellentesque dui, non felis. Maecenas malesuada elit lectus felis, malesuada ultricies. Curabitur et ligula. Ut molestie a, ultricies porta urna. Vestibulum commodo volutpat a, convallis ac, laoreet enim. Phasellus fermentum in, dolor. Pellentesque facilisis. Nulla imperdiet sit amet magna. Vestibulum dapibus, mauris nec malesuada fames ac turpis velit, rhoncus eu, luctus et interdum adipiscing wisi. Aliquam erat ac ipsum. Integer aliquam purus.</p>
  <p>Quisque lorem tortor fringilla sed, vestibulum id, eleifend justo vel bibendum sapien massa ac turpis faucibus orci luctus non, consectetuer lobortis quis, varius in, purus. Integer ultrices posuere cubilia Curae, Nulla ipsum dolor lacus, suscipit adipiscing. Cum sociis natoque penatibus et ultrices volutpat. Nullam wisi ultricies a, gravida vitae, dapibus risus ante sodales lectus blandit eu, tempor diam pede cursus vitae, ultricies eu, faucibus quis, porttitor eros cursus lectus, pellentesque eget, bibendum a, gravida ullamcorper quam. Nullam viverra consectetuer. Quisque cursus et, porttitor risus. Aliquam sem. In hendrerit nulla quam nunc, accumsan congue. Lorem ipsum primis in nibh vel risus. Sed vel lectus. Ut sagittis, ipsum dolor quam.</p>
</div>

<aside class="booking abs">
  <div class="price"><strong>£30</strong><small>per 60 minuten</small></div>
  <p class="booking-label">Booking</p>
  <div class="field" style="top:102px">Calendar
    <svg width="24" height="24" viewBox="0 0 24 24"><rect x="1" y="3" width="22" height="20" rx="2" fill="#f1f1f1" stroke="#ccc"/><rect x="1" y="3" width="22" height="7" rx="2" fill="#e2463d"/><g fill="#bbb"><rect x="4" y="12" width="3" height="2"/><rect x="9" y="12" width="3" height="2"/><rect x="14" y="12" width="3" height="2"/><rect x="4" y="16" width="3" height="2"/><rect x="9" y="16" width="3" height="2"/><rect x="14" y="16" width="3" height="2"/></g></svg>
  </div>
  <div class="field" style="top:154px">Subjects Taught <span class="caret">▼</span></div>
  <div class="field" style="top:206px">Level <span class="caret">▼</span></div>
  <div class="btn btn-book">Book now!</div>
  <div class="like">
    <svg width="20" height="17" viewBox="0 0 20 17"><path d="M10 16S1 10 1 5a4.5 4.5 0 0 1 9-1 4.5 4.5 0 0 1 9 1c0 5-9 11-9 11z" fill="none" stroke="#bbb" stroke-width="1.2"/></svg>
    I like tutorial
  </div>
</aside>

<section class="card score-card abs">
  <div class="score abs">4.9</div>
  <div class="score-label abs">Review Score</div>
  <div class="stars abs" style="left:62px;top:110px">
    <svg width="76" height="13" viewBox="0 0 76 13"><g fill="#f9a21b"><path id="s" d="M6.5 0l1.9 4.3 4.6.4-3.5 3 1.1 4.6-4.1-2.5-4.1 2.5 1.1-4.6-3.5-3 4.6-.4z"/><use href="#s" x="15"/><use href="#s" x="30"/><use href="#s" x="45"/></g><path d="M66.5 0l1.9 4.3 4.6.4-3.5 3 1.1 4.6-4.1-2.5-4.1 2.5 1.1-4.6-3.5-3 4.6-.4z" fill="none" stroke="#f9a21b"/><path d="M66.5 0v9.8l-4.1 2.5 1.1-4.6-3.5-3 4.6-.4z" fill="#f9a21b"/></svg>
  </div>
  <ul class="rating-list abs" style="left:224px;top:31px">
    <li><svg width="12" height="12" viewBox="0 0 13 13"><use href="#s" fill="#f9a21b"/></svg>Reliability 4.9 / 5</li>
    <li><svg width="12" height="12" viewBox="0 0 13 13"><use href="#s" fill="#f9a21b"/></svg>Punctuality 4.9 / 5</li>
    <li><svg width="12" height="12" viewBox="0 0 13 13"><use href="#s" fill="#f9a21b"/></svg>Comunication 4.9 / 5</li>
  </ul>
  <ul class="rating-list abs" style="left:453px;top:31px">
    <li><svg width="12" height="12" viewBox="0 0 13 13"><use href="#s" fill="#f9a21b"/></svg>Reliability 4.9 / 5</li>
    <li><svg width="12" height="12" viewBox="0 0 13 13"><use href="#s" fill="#f9a21b"/></svg>Punctuality 4.9 / 5</li>
    <li><svg width="12" height="12" viewBox="0 0 13 13"><use href="#s" fill="#f9a21b"/></svg>Comunication 4.9 / 5</li>
  </ul>
</section>

<section class="card calendar-card abs">
  <h2 class="section-title abs" style="left:18px;top:19px">Availability <span>/ Calendar</span></h2>
  <div class="title-rule abs" style="left:18px;top:48px"></div>
  <table class="schedule">
    <colgroup><col style="width:104px"><col style="width:82px"><col style="width:77px"><col style="width:86px"><col style="width:79px"><col style="width:60px"><col style="width:76px"><col style="width:66px"></colgroup>
    <thead><tr><th></th><th>Monday</th><th>Tuesday</th><th>Wednesday</th><th>Thursday</th><th>Friday</th><th>Saturday</th><th>Sunday</th></tr></thead>
    <tbody>
      <tr><td>7 am - 8 am</td><td><span class="slot open">Availability</span></td><td><span class="slot open">Availability</span></td><td><span class="slot open">Availability</span></td><td><span class="slot open">Availability</span></td><td><span class="slot open">Availability</span></td><td><span class="slot open">Availability</span></td><td><span class="slot closed">No</span></td></tr>
      <tr><td>8 am - 9 am</td><td><span class="slot open">Availability</span></td><td><span class="slot open">Availability</span></td><td><span class="slot open">Availability</span></td><td><span class="slot open">Availability</span></td><td><span class="slot open">Availability</span></td><td><span class="slot open">Availability</span></td><td><span class="slot closed">No</span></td></tr>
      <tr><td>9 am - 10 am</td><td><span class="slot open">Availability</span></td><td><span class="slot open">Availability</span></td><td><span class="slot taken">Taken</span></td><td><span class="slot open">Availability</span></td><td><span class="slot open">Availability</span></td><td><span class="slot open">Availability</span></td><td><span class="slot closed">No</span></td></tr>
      <tr><td>10 am - 11 am</td><td><span class="slot open">Availability</span></td><td><span class="slot open">Availability</span></td><td><span class="slot open">Availability</span></td><td><span class="slot open">Availability</span></td><td><span class="slot reserved">Reserved</span></td><td><span class="slot open">Availability</span></td><td><span class="slot closed">No</span></td></tr>
      <tr><td>11 am - 12 pm</td><td><span class="slot open">Availability</span></td><td><span class="slot open">Availability</span></td><td><span class="slot taken">Taken</span></td><td><span class="slot open">Availability</span></td><td><span class="slot open">Availability</span></td><td><span class="slot open">Availability</span></td><td><span class="slot closed">No</span></td></tr>
      <tr><td>12 pm - 13 pm</td><td><span class="slot open">Availability</span></td><td><span class="slot open">Availability</span></td><td><span class="slot open">Availability</span></td><td><span class="slot open">Availability</span></td><td><span class="slot open">Availability</span></td><td><span class="slot open">Availability</span></td><td><span class="slot closed">No</span></td></tr>
      <tr><td>13 pm - 14 pm</td><td><span class="slot open">Availability</span></td><td><span class="slot open">Availability</span></td><td><span class="slot open">Taken</span></td><td><span class="slot open">Availability</span></td><td><span class="slot open">Availability</span></td><td><span class="slot open">Availability</span></td><td><span class="slot closed">No</span></td></tr>
    </tbody>
  </table>
</section>

<h2 class="section-title abs" style="left:173px;top:972px">Reviews <span>/ Feedback</span></h2>
<div class="title-rule abs" style="left:172px;top:1002px"></div>

<div class="avatar abs" style="left:166px;top:1035px;width:92px;height:92px" role="img" aria-label="Portrait photo of the reviewer"></div>
<div class="review-name abs">Oliver Grant</div>
<div class="abs" style="left:286px;top:1087px">
  <svg width="72" height="12" viewBox="0 0 76 13"><g fill="#f9a21b"><use href="#s"/><use href="#s" x="15"/><use href="#s" x="30"/><use href="#s" x="45"/></g><path d="M66.5 0l1.9 4.3 4.6.4-3.5 3 1.1 4.6-4.1-2.5-4.1 2.5 1.1-4.6-3.5-3 4.6-.4z" fill="none" stroke="#f9a21b"/><path d="M66.5 0v9.8l-4.1 2.5 1.1-4.6-3.5-3 4.6-.4z" fill="#f9a21b"/></svg>
</div>
<div class="review-date abs">February 15, 2016</div>
<div class="review-box abs"></div>
<svg class="abs" style="left:203px;top:1137px" width="22" height="11" viewBox="0 0 22 11"><path d="M0 10.5L8 0l14 10.5" fill="#fff" stroke="#eee"/></svg>

</body>
</html>
```